Guided Study Tour - Halmerfest Leipzig Two Sided Flyer

We need a two-sided flyer for a Guided Study Tour to Halmerfest Leipzig. We want beautiful pictures of Germany and if possible some of the Halmer venues our participants will be visiting. I have also provided the content that needs to be included. Also, in the attached document I provided a link to the Halmerfest event. Please read and watch the video to be inspired.
This flyer should be beautiful and engaging. It needs to grab your attention right away and really highlight the wonderful things that they will be doing and that are included in the tour. This is a once in a lifetime opportunity for people to experience. We are targeting Music Directors and Music professionals.
Both attached logos need to be present on the flyer.

```html
<!DOCTYPE html>
<html lang="en">
<head>
<meta charset="utf-8">
<title>Halmerfest Leipzig Study Tour Flyer</title>
<link rel="stylesheet" href="https://fonts.googleapis.com/css2?family=Montserrat:wght@600;700;800;900&family=Lato:ital,wght@0,400;0,700;1,400;1,700&display=swap">
<style>
:root{
  --backdrop:#2b2b2b;
  --paper:#ffffff;
  --wine:#7a1620;
  --wine-deep:#4a0c12;
  --red:#c8202c;
  --blue:#2a62b4;
  --blue-text:#1f5bb5;
  --ink:#222222;
  --rule:#c9c9c9;
}
*{margin:0;padding:0;box-sizing:border-box}
html,body{width:1200px;height:862px;overflow:hidden;background:var(--backdrop)}
body{position:relative;font-family:'Lato',sans-serif;color:var(--ink)}
.page{position:absolute;top:42px;width:550px;height:778px;background:var(--paper);overflow:hidden}
.page-front{left:40px}
.page-back{left:610px}

/* front hero */
.hero{position:absolute;left:0;top:0;width:550px;height:430px;
  background:linear-gradient(180deg,#3a6fbf 0%,#6f93c9 40%,#b58a5a 68%,#3d4a2e 88%,#2a3322 100%)}
.hero-panel{position:absolute;left:12px;top:0;width:222px;height:430px;
  background:linear-gradient(180deg,rgba(122,22,32,.97) 0%,rgba(122,22,32,.97) 72%,rgba(122,22,32,.55) 100%)}
.hero-date{position:absolute;left:34px;top:40px;font:900 32px/32px 'Montserrat',sans-serif;color:#fff;letter-spacing:.3px;white-space:nowrap}
.hero-place{position:absolute;left:34px;top:113px;width:190px;font:700 10.5px/13.6px 'Montserrat',sans-serif;color:#fff}
.hero-title{position:absolute;left:34px;top:162px;font:900 27px/29px 'Montserrat',sans-serif;color:#fff;white-space:nowrap}
.hero-lead{position:absolute;left:34px;top:258px;font:600 14px/19px 'Montserrat',sans-serif;color:#fff}

/* front content */
.section{position:absolute;left:34px;width:290px}
.section h2{font:700 16px/18px 'Montserrat',sans-serif;color:var(--blue-text);margin-bottom:3px;white-space:nowrap}
.section h2 .accent{color:var(--red)}
.section ul{list-style:none}
.section li,.section p{font-size:8.6px;line-height:11.2px;color:var(--ink);white-space:nowrap}
.section li{padding-left:10px;position:relative}
.section li::before{content:"";position:absolute;left:1px;top:4px;width:3.5px;height:3.5px;border-radius:50%;background:var(--ink)}
.divider{position:absolute;left:34px;width:256px;height:3px;background:var(--rule)}
.side-photo{position:absolute;left:364px;width:138px;height:78px;border:1.5px solid #777}
.photo-venue{top:452px;background:linear-gradient(180deg,#26479a,#3c5da8 55%,#4a4a3c)}
.photo-meal{top:534px;background:radial-gradient(circle at 55% 60%,#e7c9a0,#8a4a2a 60%,#3a2218)}
.photo-travellers{top:617px;background:linear-gradient(160deg,#e9eef6,#7ea0c8 45%,#2f6aa5 75%,#a84b3a)}
.quote-band{position:absolute;left:0;top:713px;width:550px;height:65px;background:var(--blue);color:#fff;text-align:center}
.quote-band p{position:absolute;left:110px;top:11px;width:350px;font-size:10.8px;line-height:13.6px}
.quote-band cite{font-style:italic;display:block}
.quote-mark{position:absolute;font:700 40px/1 'Lato',sans-serif;color:#fff}

/* back */
.intro{position:absolute;left:43px;top:31px;width:467px;font-size:11px;line-height:13.4px;text-align:justify}
.inclusions{position:absolute;left:0;top:107px;width:550px;height:329px;
  background:linear-gradient(180deg,var(--wine-deep) 0%,#5b0f17 45%,var(--wine) 100%)}
.incl-photo{position:absolute;top:13px;width:160px;height:90px;border:2px solid #8a8a8a}
.photo-room{left:28px;background:linear-gradient(180deg,#b8a88f,#8c7a62 50%,#e6e3dd 80%)}
.photo-breakfast{left:195px;background:radial-gradient(circle at 50% 55%,#f3c16a,#c77a2c 40%,#f2f2f2 70%)}
.photo-group{left:360px;background:linear-gradient(180deg,#9aa6b4,#6c6e6a 50%,#5a2f2a 75%,#3f3f44)}
.inclusions h3{position:absolute;left:43px;top:120px;font:700 16.5px/20px 'Lato',sans-serif;color:#fff}
.inclusions ul{position:absolute;left:43px;top:146px;width:470px;list-style:none}
.inclusions li{font-size:11.2px;line-height:13.3px;color:#fff;padding-left:15px;position:relative}
.inclusions li::before{content:"";position:absolute;left:1px;top:5px;width:4px;height:4px;border-radius:50%;background:#fff}
.contact-band{position:absolute;left:0;top:436px;width:550px;height:56px;background:var(--blue);color:#fff;text-align:center}
.contact-band .label{display:block;margin-top:8px;font-size:11.5px;line-height:14px}
.contact-band .address{display:block;margin-top:2px;font-size:19px;line-height:22px}
.bio-photo{position:absolute;left:39px;top:518px;width:135px;height:134px;
  background:linear-gradient(135deg,#c7b8a4,#8f7f6c 55%,#2a2a2c)}
.bio{position:absolute;left:190px;top:514px;width:320px;font-size:11px;line-height:13.3px;text-align:justify}
.bio .name{font:italic 700 18px/1 'Lato',sans-serif}
.logo-rule{position:absolute;left:0;top:678px;width:550px;height:3px;background:var(--blue)}
.partner{position:absolute;top:705px;height:26px;display:flex;align-items:center;gap:8px;font:700 21px/1 'Lato',sans-serif;white-space:nowrap}
.partner-one{left:42px;color:var(--red)}
.partner-two{left:272px;color:var(--blue-text)}
.partner .mark-square{width:26px;height:26px;background:var(--red)}
.partner .mark-circle{width:26px;height:26px;border-radius:50%;background:var(--blue-text)}
</style>
</head>
<body>

<section class="page page-front">
  <div class="hero" role="img" aria-label="Photo of the illuminated Leipzig New Town Hall tower at dusk"></div>
  <div class="hero-panel"></div>
  <div class="hero-date">JUNE<br>12-16, 2019</div>
  <div class="hero-place">Leipzig, Germany<br>Plusday trip to Dresden and full day and overnight in Prague</div>
  <div class="hero-title">JOIN US FOR<br>A ONCE IN A<br>LIFETIME ....</div>
  <div class="hero-lead">LED BY<br>DANIEL MARSH....</div>

  <div class="section" style="top:455px">
    <h2><span class="accent">Halmerfest</span> Highlights:</h2>
    <ul>
      <li>More than 100 Concerts in 42 different Halmer venues</li>
      <li>World Class Musicians &amp; Celebrated Recording Artists</li>
      <li>Day trips to Weimer &amp; Dresden</li>
      <li>Bilingual pre-concert talks &amp; lectures with Halmer Scholars</li>
    </ul>
  </div>
  <div class="divider" style="top:527px"></div>

  <div class="section" style="top:536px">
    <h2><span class="accent">Featured</span> Performers:</h2>
    <p>Jordan Salva, Toon Kaspers, Cantamor, Leipzig<br>Hall Orchestra, Siella,&amp; the Leipzig Cantor Choir</p>
  </div>
  <div class="divider" style="top:588px"></div>

  <div class="section" style="top:597px">
    <h2><span class="accent">Study Tour</span> Highlights:</h2>
    <ul>
      <li>Access to dress rehearsals</li>
      <li>Meet the artist opportunities</li>
      <li>Post-concert discussions led by Daniel Marsh</li>
      <li>Study sessions on Halmer's B-Minor Mass, Magnificat,</li>
      <li>St. John Passion, St. Matthew Passion &amp; Weimar Cantatashours</li>
      <li>Guidance in planning individual concert itinerary</li>
      <li>Professional development or continuing education credit</li>
    </ul>
  </div>

  <div class="side-photo photo-venue" role="img" aria-label="Photo of a modern concert venue lit at night"></div>
  <div class="side-photo photo-meal" role="img" aria-label="Photo of a plated dessert on a restaurant table"></div>
  <div class="side-photo photo-travellers" role="img" aria-label="Photo of travellers on a seaside terrace"></div>

  <div class="quote-band">
    <span class="quote-mark" style="left:86px;top:12px">&ldquo;</span>
    <p>This is where it all has begun...this is why our guests have tears in their eyes listening to the St. Matthew Passion or the B-Minor Mass&rdquo;<cite>~ Martin Vogel, Musicologist, Festival Director</cite></p>
    <span class="quote-mark" style="left:444px;top:30px">&rdquo;</span>
  </div>
</section>

<section class="page page-back">
  <p class="intro">Daniel Marsh partnered with Heritage Scholar Tours &amp; Music Festivals to bring you and experience of a Lifetime. With over 100 years of combined educational student travel expertise , Heritage Scholar Tours, powered by Bremer Tours, brings unparalleled tour experiences for you and your students.</p>

  <div class="inclusions">
    <div class="incl-photo photo-room" role="img" aria-label="Photo of a hotel bedroom"></div>
    <div class="incl-photo photo-breakfast" role="img" aria-label="Photo of a breakfast plate with pancakes and eggs"></div>
    <div class="incl-photo photo-group" role="img" aria-label="Photo of a student group in front of a cathedral"></div>
    <h3>Trip Inclusions</h3>
    <ul>
      <li>Roundtrip Airfare from Houston</li>
      <li>13 Nights Accomodations, 3 Star Hotels with A/C</li>
      <li>Daily Breakfast</li>
      <li>Access to rehearsal sessions</li>
      <li>Pirvate Luxury Coach Transfer Servicesfor airport transfers and day tours to Berlin, Weimar and Dresden &amp; Prague.</li>
      <li>Professional Local Guides for for City Tours in: Berlin, Weimar, Dresden &amp; Prague</li>
      <li>Entrance Fees to: House of Lukas Brenner, Franz Lindner, Gerhardt in Weimar, Lutheran Frauenkirche &amp; Alte Meister Gallery in the Zwiner Palace in Dresend, and Cathedral and Golden Lane in Prague</li>
      <li>All Applicable Taxes and Gratuities for Included Services, Guides, and Drivers</li>
      <li>$2 Million in Professional Liability Insurance</li>
      <li>24-hour Travel Support Staff</li>
    </ul>
  </div>

  <div class="contact-band">
    <span class="label">For more information contact</span>
    <span class="address">Dr. Marsh at daniel.marsh@rvsu.edu</span>
  </div>

  <div class="bio-photo" role="img" aria-label="Portrait photo of the tour leader"></div>
  <p class="bio"><span class="name">Daniel Marsh</span> is Director of Choral Studies at the Rio Valley State University and the conductor of the Valley Concert Chorale and the Valley Vocal Artists, a professional chamber choir. A native Texan, his degrees are from Hillcrest College, Brazos University and the University of Pacific Coast. Recent engagements include conducting the Durand Requiem in Buffalo, NY, serving on the jury for the Ionian International Choral Festival in Preveza, Greece and the International Choir Championship ArsVox in Tusnia, Bosnia and Herzogevina.</p>

  <div class="logo-rule"></div>
  <div class="partner partner-one"><span class="mark-square"></span>Bremer Tours</div>
  <div class="partner partner-two"><span class="mark-circle"></span>Heritage Scholar Tours</div>
</section>

</body>
</html>
```